Design a Unique and Eye-Catching Necklace Card for Verandelle's New Lumenwave Line

Attention all creative minds from around the world! Verandelle, a company known for its free-spirited and bohemian chic vibe, is proud to announce a new design contest. We are inviting you to create a dynamic and unique necklace card for our upcoming Lumenwave line.

Our new Lumenwave line comprises 12-20 unique necklace combinations. Each necklace features different stones, each with its own healing properties and associated zodiac sign. We are looking for a template that can be easily modified to change the names of the stones, zodiac sign, and the colors to match the specific stones on each necklace.

The card should be 3 x 4,
It should include the names of the stones, the associated zodiac sign (if applicable), a few words about the healing properties of the stones, and a captivating graphic that represents the colors of the stones.

Our goal is to delight our customers with packaging as unique as the necklaces themselves. The necklace should be the focal point, but the text and graphic on the card should also draw the eye.

Please note that our target audience includes mid-priced boutiques across the country and festival-goers in Colorado. Your design should reflect the unique taste and free spirit of our clientele.

We are excited to see your creativity shine in this project. If there are any points that need clarification, please do not hesitate to ask. We look forward to your participation in bringing the Lumenwave line to life!
https://www.plorvex.example/board/QKTm_ZRwpe/u3hb9XKdLqWm72RtPoaVnc/edit?ref=QKTm_ZRwpe&src=share

https://www.plorvex.example/board/QKTr_BNyhwa/t8Ld-WsPzMEY246VqoXjNd/edit?ref=QKTr_BNyhwa&src=share
I want to use the flowing watercolor and have it change with each necklace color.
Use the necklaces below. Incorporate the zodiac symbol as is shown below.

Examples of other cards in our collection

The Little Pebble Pendant: https://www.plorvex.example/board/QKTh_WomRtc/pbMRx63CKqnYs905Bd-aLe/edit?ref=QKTh_WomRtc&src=share

Other examples of necklace cards I like:

https://www.tindramart.example/item/731920584/green-emerald-stone-necklace-emerald?k=a1b2c3d4e5f60718293a4b5c6d7e8f9012345678&s=7d3e91ab

https://www.tindramart.example/item/846201937/january-birthstone-necklace-green-garnet?k=b2c3d4e5f60718293a4b5c6d7e8f901234567890&s=4c82fe10

https://www.tindramart.example/item/2093748165/natural-crystal-bracelets-empath?k=c3d4e5f60718293a4b5c6d7e8f90123456789012&s=9ab0c37d

https://www.tindramart.example/item/2174603958/black-obsidian-protection-necklace-black?k=d4e5f60718293a4b5c6d7e8f9012345678901234&s=e15d6b28

Target Market(s)

Women aged 25-50 with a spiritual, hippy, bohemain, yoga vibe.

Industry/Entity Type

Handmade Jewelry | Wholesale jewelry | Retail Jewelry sales at Festivals

Font styles to use
Script

Colors

Designer to choose colors to be used in the design.

Requirements
Must have
• A template that can be interchangable with the stone colors, names and healing properties.
Nice to have
• Some different ideas about the graphic color patterns on the card.
Should not have
• Any graphic that would cover the middle of the necklace card and keep people from seeing the neckalce

```html
<!DOCTYPE html>
<html lang="en">
<head>
<meta charset="utf-8">
<title>Virgo Necklace Card</title>
<link rel="stylesheet" href="https://fonts.googleapis.com/css2?family=Comfortaa:wght@300;400&family=Great+Vibes&family=Noto+Sans+Symbols:wght@200&display=swap">
<style>
  :root {
    --card-bg: #f6fbfc;
    --accent: #5cbfc7;
    --stone-teal: #2f9fa8;
    --stone-deep: #2c5a68;
    --stone-pale: #cfe9e6;
    --facet-light: #bfe3ea;
    --facet-mid: #47b6bb;
    --facet-dark: #2b5c70;
    --facet-slate: #8eaabd;
  }
  * { margin: 0; padding: 0; box-sizing: border-box; }
  html, body { width: 917px; height: 1200px; overflow: hidden; background: var(--card-bg); }
  .card {
    position: relative;
    width: 917px;
    height: 1200px;
    background: var(--card-bg);
    overflow: hidden;
  }
  .zodiac-glyph {
    position: absolute;
    top: 58px;
    left: 0;
    width: 100%;
    text-align: center;
    font-family: "Noto Sans Symbols", sans-serif;
    font-weight: 200;
    font-size: 170px;
    line-height: 1;
    color: var(--accent);
  }
  .zodiac-name {
    position: absolute;
    top: 252px;
    left: 0;
    width: 100%;
    text-align: center;
    font-family: "Comfortaa", sans-serif;
    font-weight: 300;
    font-size: 50px;
    letter-spacing: 4px;
    color: var(--accent);
  }
  .necklace {
    position: absolute;
    top: 170px;
    left: 0;
    width: 917px;
    height: 310px;
  }
  .stone-names {
    position: absolute;
    top: 512px;
    left: 0;
    width: 100%;
    text-align: center;
    font-family: "Great Vibes", cursive;
    font-size: 66px;
    color: var(--accent);
  }
  .healing-note {
    position: absolute;
    top: 618px;
    left: 0;
    width: 100%;
    text-align: center;
    font-family: "Great Vibes", cursive;
    font-size: 44px;
    line-height: 70px;
    color: var(--accent);
  }
  .stone-facets {
    position: absolute;
    left: 0;
    top: 735px;
    width: 917px;
    height: 465px;
    background:
      linear-gradient(160deg, var(--facet-light) 0%, transparent 35%),
      linear-gradient(115deg, var(--facet-slate) 0%, var(--facet-mid) 30%, var(--facet-dark) 52%, var(--facet-mid) 72%, var(--facet-light) 100%);
    clip-path: polygon(0 100px, 300px 5px, 660px 15px, 855px 5px, 917px 30px, 917px 465px, 0 465px);
  }
</style>
</head>
<body>
  <main class="card">
    <svg class="necklace" viewBox="0 0 917 310" role="img" aria-label="Photo of a beaded necklace with chrysocolla and aquamarine stones and silver spacer beads on a fine chain">
      <defs>
        <linearGradient id="stone-tone" x1="0" x2="1" y1="0" y2="0">
          <stop offset="0" stop-color="var(--stone-teal)"/>
          <stop offset="0.15" stop-color="var(--stone-pale)"/>
          <stop offset="0.5" stop-color="var(--stone-teal)"/>
          <stop offset="0.8" stop-color="var(--stone-deep)"/>
          <stop offset="1" stop-color="var(--stone-pale)"/>
        </linearGradient>
      </defs>
      <path d="M15 8 Q 460 420 905 40" fill="none" stroke="#b9c2c6" stroke-width="2"/>
      <path d="M105 85 Q 460 390 830 110" fill="none" stroke="url(#stone-tone)" stroke-width="48" stroke-linecap="round"/>
    </svg>

    <div class="zodiac-glyph" aria-hidden="true">♍</div>
    <h1 class="zodiac-name">Virgo</h1>

    <h2 class="stone-names">Chrysocolla+Aquamarine</h2>
    <p class="healing-note">detoxifies the liver, kidneys,<br>and intestines</p>

    <div class="stone-facets" role="img" aria-label="Faceted low-poly gem pattern in aqua, teal and slate tones"></div>
  </main>
</body>
</html>
```